Corvane spray foam and Environmental

I have business cards but need new ones. The ones I have are very bland. Here is. Y company website http://www.corvanesprayfoam.ca

Also I can send you copies of the current cards
I would also need my current logo on the new design as well.. Also spray foam and Environmental

Industry/Entity Type

Business

Logo Text

Corvane.

```html
<!DOCTYPE html>
<html lang="en">
<head>
<meta charset="utf-8">
<title>Corvane business cards</title>
<link rel="stylesheet" href="https://fonts.googleapis.com/css2?family=Open+Sans:wght@700&family=Roboto:wght@400;500;700&display=swap">
<style>
  :root {
    --bg: #2b0a3d;
    --card: #ffffff;
    --purple: #5b1f6b;
    --purple-light: #6f3f8e;
    --slate: #42464d;
    --grey: #a9abb0;
    --text: #4a4a4f;
  }
  * { margin: 0; padding: 0; box-sizing: border-box; }
  html, body { width: 1200px; height: 1200px; overflow: hidden; }
  body { background: var(--bg); position: relative; font-family: "Roboto", Arial, sans-serif; }
  .card {
    position: absolute; left: 170px; width: 860px; height: 505px;
    background: var(--card); overflow: hidden;
  }
  .card--front { top: 70px; }
  .card--back { top: 625px; }
  .corner { position: absolute; }
  .corner--top { top: 0; left: 0; }
  .corner--bottom { bottom: 0; right: 0; }
  .mark-square { position: absolute; background: var(--slate); }
  .wordmark {
    position: absolute; font-family: "Open Sans", Arial, sans-serif; font-weight: 700;
    color: var(--purple); letter-spacing: -1px; line-height: 1;
  }
  .card--front .mark-square { left: 345px; top: 140px; width: 160px; height: 130px; }
  .card--front .wordmark { left: 0; width: 100%; text-align: center; top: 285px; font-size: 96px; }
  .card--back .mark-square { left: 166px; top: 59px; width: 122px; height: 100px; }
  .card--back .wordmark { left: 80px; top: 168px; font-size: 70px; }
  .contact { position: absolute; left: 80px; }
  .contact--foam { top: 268px; }
  .contact--env { top: 384px; }
  .contact h3 { font-size: 15px; font-weight: 700; color: var(--purple); margin-bottom: 6px; }
  .contact li { list-style: none; display: flex; align-items: center; gap: 14px; font-size: 12px; color: var(--text); height: 22px; }
  .contact svg { width: 13px; height: 13px; fill: none; stroke: var(--slate); stroke-width: 2; }
  .contact-rule { position: absolute; left: 80px; top: 360px; width: 182px; height: 2px; background: var(--purple-light); }
  .service { position: absolute; left: 497px; border-left: 2px solid var(--grey); padding-left: 24px; }
  .service--foam { top: 72px; }
  .service--env { top: 298px; }
  .service h2 { font-family: "Roboto", Arial, sans-serif; font-size: 31px; font-weight: 700; color: var(--purple); line-height: 1.2; margin-bottom: 8px; }
  .service li { list-style: none; font-size: 14px; line-height: 20.7px; color: var(--text); }
</style>
</head>
<body>

<section class="card card--front" aria-label="Card front">
  <svg class="corner corner--top" width="116" height="102"><polygon points="0,0 116,0 0,102" fill="#6f3f8e"/></svg>
  <div class="mark-square"></div>
  <div class="wordmark">CORVANE</div>
  <svg class="corner corner--bottom" width="102" height="112"><polygon points="102,0 102,112 0,112" fill="#42464d"/></svg>
</section>

<section class="card card--back" aria-label="Card back">
  <svg class="corner corner--top" width="114" height="103"><polygon points="0,0 114,0 0,103" fill="#6f3f8e"/></svg>
  <div class="mark-square"></div>
  <div class="wordmark">CORVANE</div>

  <div class="contact contact--foam">
    <h3>SPRAY FOAM</h3>
    <ul>
      <li><svg viewBox="0 0 16 16"><path d="M3 2l3 0 1 3-2 1.5a8 8 0 0 0 4.5 4.5L11 9l3 1v3l-1.5 1.5C6 14 2 10 1.5 3.5z"/></svg>(604) 555-0147</li>
      <li><svg viewBox="0 0 16 16"><rect x="1.5" y="3.5" width="13" height="9"/><path d="M1.5 3.5l6.5 5 6.5-5"/></svg>corvanefoam@example.com</li>
      <li><svg viewBox="0 0 16 16"><circle cx="8" cy="8" r="6.5"/><path d="M1.5 8h13M8 1.5c-3 3.5-3 9.5 0 13M8 1.5c3 3.5 3 9.5 0 13"/></svg>www.corvanesprayfoam.ca</li>
    </ul>
  </div>
  <div class="contact-rule"></div>
  <div class="contact contact--env">
    <h3>ENVIRONMENTAL</h3>
    <ul>
      <li><svg viewBox="0 0 16 16"><path d="M3 2l3 0 1 3-2 1.5a8 8 0 0 0 4.5 4.5L11 9l3 1v3l-1.5 1.5C6 14 2 10 1.5 3.5z"/></svg>(604) 555-0182</li>
      <li><svg viewBox="0 0 16 16"><rect x="1.5" y="3.5" width="13" height="9"/><path d="M1.5 3.5l6.5 5 6.5-5"/></svg>corvaneenviro1@example.com</li>
      <li><svg viewBox="0 0 16 16"><circle cx="8" cy="8" r="6.5"/><path d="M1.5 8h13M8 1.5c-3 3.5-3 9.5 0 13M8 1.5c3 3.5 3 9.5 0 13"/></svg>www.corvaneenvironmental.ca</li>
    </ul>
  </div>

  <div class="service service--foam">
    <h2>SPRAY FOAM</h2>
    <ul>
      <li>Roofing fam</li>
      <li>Slabjacking</li>
      <li>2pound/ Half Pound</li>
      <li>Sound Proofing</li>
      <li>Batt Insulation</li>
      <li>Attic Blow In</li>
    </ul>
  </div>
  <div class="service service--env">
    <h2>ENVIRONMENTAL</h2>
    <ul>
      <li>Air Monitoring</li>
      <li>Asbestos Testing</li>
      <li>Asbestos Removal</li>
      <li>Building Demolition</li>
      <li>Lead Testing</li>
      <li>Mould Removal</li>
    </ul>
  </div>

  <svg class="corner corner--bottom" width="105" height="113"><polygon points="105,0 105,113 0,113" fill="#42464d"/></svg>
</section>

</body>
</html>
```